Business Card Design

I'm after a modern and artistic business card design, with clean lines and popping colour. The business card should be professional looking and promote my business.

```html
<!DOCTYPE html>
<html lang="en">
<head>
<meta charset="utf-8">
<title>Rosalind – Make Up Artist Business Card</title>
<link rel="stylesheet" href="https://fonts.googleapis.com/css2?family=Federo&family=Quicksand:wght@500;600&display=swap">
<style>
  :root {
    --page: #e9e6e2;
    --card-dark: #050505;
    --card-light: #ffffff;
    --ink: #111111;
    --ink-soft: #2a2a2a;
    --swirl: #d9d9d9;
    --hair: #6b4a2c;
    --skin: #d9b39a;
    --jacket: #7a4a26;
    --blush: #e58a8f;
    --petal: #f3a3c3;
  }
  * { box-sizing: border-box; margin: 0; padding: 0; }
  html, body {
    width: 1200px; height: 803px; overflow: hidden;
    background: var(--page);
  }
  .sheet {
    position: relative; width: 1200px; height: 803px;
    display: flex; align-items: center; justify-content: center; gap: 30px;
  }
  .card {
    position: relative; width: 560px; height: 342px; overflow: hidden;
  }

  /* Back of card */
  .card--back { background: var(--card-dark); }
  .card__ornament {
    position: absolute; inset: 0;
    background:
      radial-gradient(ellipse 180px 150px at 170px 110px, rgba(217,217,217,.22), transparent 70%),
      radial-gradient(ellipse 140px 110px at 470px 90px, rgba(217,217,217,.16), transparent 70%),
      radial-gradient(ellipse 260px 80px at 200px 320px, rgba(217,217,217,.2), transparent 70%),
      radial-gradient(ellipse 120px 120px at 520px 270px, rgba(217,217,217,.14), transparent 70%);
  }
  .card__title {
    position: absolute; left: 0; right: 0; top: 134px;
    text-align: center;
    font-family: "Federo", sans-serif; font-size: 44px;
    color: var(--swirl); letter-spacing: 1px;
  }

  /* Front of card */
  .card--front { background: var(--card-light); }
  .card__portrait {
    position: absolute; left: 0; top: 0; width: 250px; height: 100%;
    background:
      linear-gradient(90deg, rgba(255,255,255,0) 60%, var(--card-light) 100%),
      linear-gradient(180deg, var(--hair) 0%, var(--skin) 30%, var(--skin) 62%, var(--jacket) 85%, var(--jacket) 100%);
  }
  .card__products {
    position: absolute; left: 328px; top: 6px; width: 120px; height: 78px;
    background: radial-gradient(ellipse at 45% 60%, var(--blush), rgba(229,138,143,0) 70%);
  }
  .card__flower {
    position: absolute; left: 478px; top: 0; width: 80px; height: 64px;
    background: radial-gradient(circle at 50% 50%, var(--petal), rgba(243,163,195,0) 70%);
  }
  .card__name {
    position: absolute; left: 284px; top: 146px;
    font-family: "Quicksand", sans-serif; font-weight: 600; font-size: 29px;
    color: var(--ink); letter-spacing: .5px;
  }
  .card__rule {
    position: absolute; left: 244px; right: 0; top: 178px;
    height: 4px; background: var(--ink);
  }
  .card__role {
    position: absolute; left: 370px; top: 183px;
    font-family: "Quicksand", sans-serif; font-weight: 600; font-size: 14px;
    color: var(--ink-soft);
  }
  .contact {
    position: absolute; left: 380px; top: 274px;
    list-style: none;
    font-family: "Quicksand", sans-serif; font-weight: 500; font-size: 14px;
    color: var(--ink);
  }
  .contact__item { display: flex; align-items: center; gap: 7px; height: 21px; }
  .contact__icon { width: 14px; height: 14px; flex: none; }
</style>
</head>
<body>
<main class="sheet">

  <section class="card card--back" aria-label="Card back">
    <div class="card__ornament" role="img" aria-label="White flowing swirl ornaments with a stylised face profile"></div>
    <h1 class="card__title">make up artist</h1>
  </section>

  <section class="card card--front" aria-label="Card front">
    <div class="card__portrait" role="img" aria-label="Portrait photograph of a model with windswept hair"></div>
    <div class="card__products" role="img" aria-label="Photograph of a blush brush and loose pink powder"></div>
    <div class="card__flower" role="img" aria-label="Photograph of a pink frangipani flower"></div>

    <h2 class="card__name">ROSALIND</h2>
    <div class="card__rule"></div>
    <p class="card__role">MAKE UP ARTIST</p>

    <ul class="contact">
      <li class="contact__item">
        <svg class="contact__icon" viewBox="0 0 14 14"><rect x="1" y="3" width="12" height="8" fill="var(--ink)"/><path d="M1 3 L7 8 L13 3" fill="none" stroke="#fff" stroke-width="1.2"/></svg>
        rosalind@mailbox.com
      </li>
      <li class="contact__item">
        <svg class="contact__icon" viewBox="0 0 14 14"><path d="M3 1 L5.5 1 L6.5 4 L5 5.2 Q6.5 8.2 8.8 9 L10 7.5 L13 8.5 L13 11 Q13 13 11 13 Q2 12 1 3 Q1 1 3 1 Z" fill="var(--ink)"/></svg>
        +61 x xxxx xxxx
      </li>
      <li class="contact__item">
        <svg class="contact__icon" viewBox="0 0 14 14"><circle cx="7" cy="7" r="5.8" fill="none" stroke="var(--ink)" stroke-width="1.3"/><ellipse cx="7" cy="7" rx="2.4" ry="5.8" fill="none" stroke="var(--ink)" stroke-width="1.1"/><path d="M1.2 7 H12.8" stroke="var(--ink)" stroke-width="1.1"/></svg>
        rosalindmakeup.com
      </li>
    </ul>
  </section>

</main>
</body>
</html>
```